Web site for Tree Removal Company

What we are looking for:
-------------------------------
Looking for a wordpress web site, you can provide your own template or we can supply you with one (http://quorvel.plindatheme.net).

What we do
---------------
To see what we do please go to google Australia and google "Tree removal Sydney" or "Tree Removal Melbourne".

Web site requirements
-----------------------------
We prefer you to use our template as it has all our requirements in already.
- Responsive.
- Based on Wordpress.
- Full complaint and compatible with plugs.

Look, Feel and Appearance
------------------------------------
Please use the logo (see attached), for colour scheme, look and feel of the web site.

Thank you for your time and effort!

Target Market(s)

Tree Removal for Residential Homes

Industry/Entity Type

It Company

Number of Pages Required

4 page

Font styles to use
Serif
Sans Serif

Requirements
Must have
• Wordpress
Nice to have
• Original artwork, images and text
Should not have
• non related images or wording

```html
<!DOCTYPE html>
<html lang="en">
<head>
<meta charset="utf-8">
<title>Timberline – Tree Removal</title>
<link href="https://fonts.googleapis.com/css2?family=Kaushan+Script&family=Roboto:wght@400;500;700&display=swap" rel="stylesheet">
<style>
:root{
  --dark:#1e2622;
  --green:#3e9a6c;
  --green-deep:#2f7d55;
  --band:rgba(42,110,74,.82);
  --text:#555;
  --heading:#2b2b2b;
  --white:#fff;
  --footer:#23292a;
}
*{box-sizing:border-box;margin:0;padding:0}
html,body{width:750px;height:1200px;overflow:hidden}
body{font-family:"Roboto",Arial,sans-serif;color:var(--text);background:#fff;position:relative}
.site-header{position:absolute;top:0;left:0;width:750px;height:75px;background:var(--dark);display:flex;align-items:center;justify-content:space-between;padding:0 30px}
.brand{display:flex;align-items:center;gap:10px;color:var(--white);font-size:14px;font-weight:500;letter-spacing:2px}
.brand-dot{width:30px;height:30px;border-radius:50%;background:var(--green)}
.main-nav{display:flex;gap:6px;height:75px;align-items:stretch}
.main-nav a{color:var(--white);text-decoration:none;font-size:11px;font-weight:500;letter-spacing:.5px;padding:0 14px;display:flex;align-items:center;border-top:4px solid transparent}
.main-nav a.active{border-top-color:var(--green);background:rgba(255,255,255,.06)}
.hero{position:absolute;top:75px;left:0;width:750px;height:387px;background:linear-gradient(100deg,#5a3424 0%,#8c5a3a 22%,#c9a070 40%,#a9b66e 52%,#6f4330 68%,#a36a44 84%,#4f2e20 100%)}
.hero-band{position:absolute;top:115px;left:200px;width:350px;height:42px;background:var(--band);display:flex;align-items:center;justify-content:center}
.hero-title{font-family:"Kaushan Script",cursive;color:var(--white);font-size:30px;font-weight:400}
.hero-text{position:absolute;top:164px;left:160px;width:430px;color:var(--white);font-size:10.5px;line-height:1.45;text-align:center;text-shadow:0 1px 2px rgba(0,0,0,.5)}
.hero-arrows{position:absolute;top:228px;left:345px;display:flex;gap:8px}
.hero-arrows span{width:24px;height:24px;border-radius:50%;background:var(--white);display:flex;align-items:center;justify-content:center}
.features{position:absolute;top:462px;left:0;width:750px;height:263px;display:flex;justify-content:space-between;padding:40px 60px 0}
.feature{width:175px;text-align:center}
.feature-icon{height:40px;display:flex;align-items:center;justify-content:center;color:var(--heading);font-size:34px;font-weight:500}
.feature h3{font-family:"Kaushan Script",cursive;font-weight:400;font-size:19px;color:var(--heading);margin:6px 0 6px}
.feature p{font-size:9.5px;line-height:1.45}
.btn{display:inline-block;margin-top:12px;background:var(--green);color:var(--white);font-size:9px;padding:5px 16px;text-decoration:none}
.work{position:absolute;top:725px;left:0;width:750px;height:200px;background:linear-gradient(100deg,#b8402e 0%,#c86c4a 30%,#8a3f52 60%,#3b4a8a 100%)}
.section-title{font-family:"Kaushan Script",cursive;font-weight:400;color:var(--heading);font-size:24px;text-align:center}
.work .section-title{padding-top:14px}
.work-grid{position:absolute;top:45px;left:50px;display:flex;gap:12px}
.work-card{width:208px;height:120px;position:relative}
.work-card .photo{position:absolute;inset:0}
.work-card .caption{position:absolute;left:0;bottom:0;width:100%;height:24px;background:rgba(30,30,30,.75);color:var(--white);font-size:10px;font-weight:500;display:flex;align-items:center;justify-content:center;letter-spacing:.5px}
.work-dots{position:absolute;top:177px;left:0;width:750px;display:flex;justify-content:center;gap:6px}
.work-dots span{width:7px;height:7px;border-radius:50%;background:rgba(255,255,255,.5)}
.work-dots span.on{background:var(--white)}
.testimonials{position:absolute;top:925px;left:0;width:750px;height:237px}
.testimonials .section-title{padding-top:24px}
.testimonial-row{display:flex;justify-content:center;gap:110px;margin-top:20px}
.testimonial{width:240px;text-align:center}
.avatar{width:46px;height:46px;border-radius:50%;margin:0 auto;border:2px solid #ddd}
.testimonial h4{font-family:"Kaushan Script",cursive;font-weight:400;font-size:13px;color:var(--heading);margin:10px 0 6px}
.testimonial p{font-size:9.5px;line-height:1.45}
.site-footer{position:absolute;top:1162px;left:0;width:750px;height:38px;background:var(--footer);display:flex;align-items:center;justify-content:space-between;padding:0 20px;color:#bbb;font-size:9px}
.social{display:flex;gap:5px}
.social span{width:16px;height:16px;display:block}
</style>
</head>
<body>
<header class="site-header">
  <div class="brand"><span class="brand-dot"></span>TIMBERLINE</div>
  <nav class="main-nav">
    <a href="#" class="active">HOME</a>
    <a href="#">TREE SERVICES</a>
    <a href="#">SAFETY</a>
    <a href="#">PAGE</a>
    <a href="#">CONTACT</a>
  </nav>
</header>

<section class="hero" role="img" aria-label="Photo of tall redwood trunks in a sunlit forest">
  <div class="hero-band"><h1 class="hero-title">Finibus Bonorum et</h1></div>
  <p class="hero-text">Lorem ipsum dolor sit amet, consectetur adipiscing elit, sed do eiusmod tempor incididunt ut labore et dolore magna aliqua. Ut enim ad minim veniam, quis nostrud exercitation.</p>
  <div class="hero-arrows">
    <span><svg width="10" height="10" viewBox="0 0 10 10"><path d="M6.5 1.5 3 5l3.5 3.5" fill="none" stroke="#222" stroke-width="1.8"/></svg></span>
    <span><svg width="10" height="10" viewBox="0 0 10 10"><path d="M3.5 1.5 7 5 3.5 8.5" fill="none" stroke="#222" stroke-width="1.8"/></svg></span>
  </div>
</section>

<section class="features">
  <div class="feature">
    <div class="feature-icon"><svg width="32" height="32" viewBox="0 0 24 24"><path d="M2 10h4v12H2zM8 21V10l5-8c1.5 0 2.5 1 2 3l-1 4h6c1.2 0 2 1 1.8 2.2l-1.6 8C20 20.3 19.2 21 18 21z" fill="#2b2b2b"/></svg></div>
    <h3>Ethical</h3>
    <p>Lorem ipsum dolor sit amet, consectetur adipiscing elit, sed do eiusmod tempor incididunt ut labore et dolore magna aliqua.</p>
    <a class="btn" href="#">More</a>
  </div>
  <div class="feature">
    <div class="feature-icon">$</div>
    <h3>Affordable</h3>
    <p>Lorem ipsum dolor sit amet, consectetur adipiscing elit, sed do eiusmod tempor incididunt ut labore et dolore magna aliqua.</p>
    <a class="btn" href="#">More</a>
  </div>
  <div class="feature">
    <div class="feature-icon"><svg width="30" height="30" viewBox="0 0 24 24"><path d="M2 13l7 7L22 5" fill="none" stroke="#2b2b2b" stroke-width="4"/></svg></div>
    <h3>Free Mulch</h3>
    <p>Lorem ipsum dolor sit amet, consectetur adipiscing elit, sed do eiusmod tempor incididunt ut labore et dolore magna aliqua.</p>
    <a class="btn" href="#">More</a>
  </div>
</section>

<section class="work">
  <h2 class="section-title">Our Work</h2>
  <div class="work-grid">
    <div class="work-card"><div class="photo" role="img" aria-label="Arborist climbing a tree trunk" style="background:linear-gradient(160deg,#4f8fc9,#7aa86a 60%,#5a6b3a)"></div><div class="caption">NEQUE PORRO QUIS</div></div>
    <div class="work-card"><div class="photo" role="img" aria-label="Worker cutting a large branch with a chainsaw" style="background:linear-gradient(160deg,#6a8a4a,#8a6a4a 55%,#b0483a)"></div><div class="caption">FINIBUS BONORUM ET</div></div>
    <div class="work-card"><div class="photo" role="img" aria-label="Stack of cut log ends" style="background:linear-gradient(160deg,#d8d6cf,#a9a59c 55%,#6e6a62)"></div><div class="caption">TEMPORIBUS AUTEM</div></div>
  </div>
  <div class="work-dots"><span class="on"></span><span></span></div>
</section>

<section class="testimonials">
  <h2 class="section-title">Customer Satisfaction</h2>
  <div class="testimonial-row">
    <div class="testimonial">
      <div class="avatar" role="img" aria-label="Portrait of a male customer" style="background:#7d7f86"></div>
      <h4>Jhon Doe</h4>
      <p>Lorem ipsum dolor sit amet, consectetur adipiscing elit, sed do eiusmod tempor incididunt ut labore et dolore magna aliqua. Ut enim ad minim veniam, quis nostrud exercitation.</p>
    </div>
    <div class="testimonial">
      <div class="avatar" role="img" aria-label="Portrait of a female customer" style="background:#b08468"></div>
      <h4>Jhon Doe</h4>
      <p>Lorem ipsum dolor sit amet, consectetur adipiscing elit, sed do eiusmod tempor incididunt ut labore et dolore magna aliqua. Ut enim ad minim veniam, quis nostrud exercitation.</p>
    </div>
  </div>
</section>

<footer class="site-footer">
  <span>2015 Copyright. All Rights Reserved.</span>
  <div class="social">
    <span style="background:#4a9fd6"></span>
    <span style="background:#e07a2e"></span>
    <span style="background:#3b5a9a"></span>
    <span style="background:#d0443a"></span>
  </div>
</footer>
</body>
</html>
```